create a book cover titled "bright canyon drift"

>>>>Updated Description>>>>>
I need conceptually enriched and minimal book cover design that hopefully represents the theme on the front page, The book is about romanticizing greenery and forests. It's a novel based on life of botanical creatures and their interaction. Think of it as a role playing novel where you(the reader) will be experiencing the story and life of botany. Book is also accompanied by a series of soundtracks which will be embedded through some secondary medium within the book.
- The cover should be simple and very minimal and could be orignal illustration
- Only design front cover, inner content and back cover design details will be shared with the winning designer only.
- Don't do any ornamanation
- It should be very too the point and clean
- hit me up incase of any confusions and ask me to clarify anything, I am here to help you out,feel free to post but design isn't really my thing so you've 100% creative freedom, I just want the design of the book cover to represent my ideas visually.
- dimensions 5.5x8

Please view the updated brief. Please alter your designs accordingly. Best Regards

Target Market(s)

adults

Font styles to use
Serif
Sans Serif

Colors

Designer to choose colors to be used in the design.

Requirements
Must have
• - Minimal design
• - Clean text
• - Bold Imagery
Nice to have
• Illustrations
Should not have
• - Dark colors
• - something abstract
• - Contentless elements

```html
<!DOCTYPE html>
<html lang="en">
<head>
<meta charset="utf-8">
<title>Bright Canyon Drift — Book Cover</title>
<link rel="stylesheet" href="https://fonts.googleapis.com/css2?family=Bebas+Neue&display=swap">
<style>
  :root {
    --backdrop: #e4e3df;
    --paper: #ffffff;
    --ink: #48484a;
    --photo-light: #f2f2f2;
    --photo-mid: #b9b9b9;
    --photo-dark: #5e5e5e;
    --leaf-veil: rgba(162, 206, 70, 0.34);
  }
  * { margin: 0; padding: 0; box-sizing: border-box; }
  html, body {
    width: 1200px;
    height: 1106px;
    overflow: hidden;
    background: var(--backdrop);
  }
  .cover {
    position: absolute;
    left: 253px;
    top: 33px;
    width: 694px;
    height: 1040px;
    background: var(--paper);
    overflow: hidden;
    font-family: "Bebas Neue", "Oswald", sans-serif;
    color: var(--ink);
  }
  .cover-photo {
    position: absolute;
    left: 0;
    top: 0;
    width: 694px;
    height: 463px;
    background:
      radial-gradient(ellipse at 18% 40%, var(--photo-light) 0%, rgba(242,242,242,0) 45%),
      linear-gradient(180deg, var(--photo-mid) 0%, var(--photo-light) 35%, var(--photo-mid) 70%, var(--photo-dark) 100%);
  }
  .title-line {
    position: absolute;
    display: flex;
    justify-content: space-between;
    line-height: 1;
    white-space: nowrap;
  }
  .title-line--first {
    left: 38px;
    right: 12px;
    top: 10px;
    font-size: 203px;
  }
  .title-line--second {
    left: 38px;
    right: 37px;
    top: 447px;
    font-size: 107px;
  }
  .title-line--third {
    left: 38px;
    right: 14px;
    top: 895px;
    font-size: 117px;
  }
  .leaf-veil {
    position: absolute;
    left: 160px;
    top: 83px;
    width: 534px;
    height: 454px;
    background: var(--leaf-veil);
  }
</style>
</head>
<body>
  <main class="cover">
    <div class="cover-photo" role="img" aria-label="Close-up photograph of a walker's trail shoes stepping along a mossy forest path, in soft grey tones"></div>

    <h1 class="book-title" aria-label="Bright Canyon Drift">
      <span class="title-line title-line--first" aria-hidden="true"><span>B</span><span>R</span><span>I</span><span>G</span><span>H</span><span>T</span></span>
      <span class="title-line title-line--second" aria-hidden="true"><span>C</span><span>A</span><span>N</span><span>Y</span><span>O</span><span>N</span></span>
      <span class="title-line title-line--third" aria-hidden="true"><span>D</span><span>R</span><span>I</span><span>F</span><span>T</span></span>
    </h1>

    <div class="leaf-veil"></div>
  </main>
</body>
</html>
```